Design BRVMentoring.com

Looking to build a business professional coach website arround Vendrixo.com , it will some standard pages, about me, a page or 2 on vendrixo, maybe with a download and email grab, contact me....

```html
<!DOCTYPE html>
<html lang="en">
<head>
<meta charset="utf-8">
<title>BRV Mentoring</title>
<link href="https://fonts.googleapis.com/css2?family=Poppins:wght@400;500;600;700&display=swap" rel="stylesheet">
<style>
:root{
  --purple:#5b2d8e;
  --green:#8cc63f;
  --blue:#1a7cc1;
  --orange:#f5a623;
  --brown:#8b5a2b;
  --black:#0b0b0b;
  --white:#ffffff;
  --ink:#222222;
}
*{box-sizing:border-box;margin:0;padding:0}
html,body{width:1200px;height:3560px;overflow:hidden}
body{font-family:'Poppins',sans-serif;color:var(--ink);background:var(--white);position:relative}

/* header */
.topbar{position:absolute;left:0;top:0;width:1200px;height:152px;background:var(--white)}
.brand{position:absolute;left:40px;top:34px;display:flex;align-items:center;gap:14px}
.brand-dot{width:60px;height:60px;border-radius:50%;background:var(--purple);flex:none}
.brand-name{font-weight:700;font-size:34px;color:var(--purple);line-height:1;white-space:nowrap}
.brand-sub{font-size:16px;color:var(--purple);margin-top:4px}
.nav{position:absolute;left:480px;top:26px;display:flex;gap:44px;font-size:18px;font-weight:500}
.btn-download{position:absolute;left:960px;top:18px;width:140px;height:44px;background:var(--green);color:var(--white);font-weight:600;font-size:17px;display:flex;align-items:center;justify-content:center}
.infobar{position:absolute;left:420px;top:76px;width:780px;height:76px;background:var(--purple);clip-path:polygon(60px 0,100% 0,100% 100%,0 100%);display:flex;align-items:center;gap:34px;padding-left:84px;color:var(--white);font-size:14px;font-weight:500;white-space:nowrap}
.info-item{display:flex;align-items:center;gap:10px}
.info-icon{width:30px;height:30px;border-radius:50%;background:var(--white);display:flex;align-items:center;justify-content:center;flex:none}

/* hero */
.hero{position:absolute;left:0;top:152px;width:1200px;height:648px;background:linear-gradient(135deg,#b9a48a 0%,#8e7a66 40%,#5e5248 100%)}
.hero-shade{position:absolute;inset:0;background:rgba(20,15,30,.35)}
.hero-text{position:absolute;left:0;width:1200px;top:196px;text-align:center;color:var(--white);font-weight:700;font-size:50px;line-height:1.15}
.btn-start{position:absolute;left:470px;top:330px;width:160px;height:50px;background:var(--purple);color:var(--white);font-weight:600;font-size:17px;display:flex;align-items:center;justify-content:center}

/* services */
.section-title{position:absolute;left:0;width:1200px;text-align:center;font-weight:700;font-size:34px;color:var(--ink)}
.service{position:absolute;top:970px;width:280px;height:220px;background:var(--white);border:1px solid #d7d7d7;box-shadow:0 4px 10px rgba(0,0,0,.12)}
.service-top{height:6px}
.service-icon{display:flex;justify-content:center;margin-top:26px}
.service-label{position:absolute;left:30px;right:30px;bottom:24px;height:44px;display:flex;align-items:center;justify-content:center;gap:16px;color:var(--white);font-weight:600;font-size:17px}

/* about */
.about{position:absolute;left:0;top:1272px;width:1200px;height:430px;background:var(--purple)}
.about-photo{position:absolute;left:700px;top:0;width:560px;height:430px;border-radius:215px 0 0 215px;background:linear-gradient(120deg,#d8d3cc,#a79886 55%,#6f6457);border:10px solid var(--white);border-right:none}
.about h2{position:absolute;left:90px;top:50px;color:var(--white);font-size:40px;font-weight:700}
.about p{position:absolute;left:90px;top:118px;width:560px;color:var(--white);font-size:15px;line-height:1.75}
.btn-read{position:absolute;left:90px;top:314px;width:130px;height:38px;background:var(--white);color:var(--ink);font-weight:600;font-size:14px;display:flex;align-items:center;justify-content:center}

/* how it works */
.step{position:absolute;top:1860px;width:250px;text-align:center}
.step-circle{width:184px;height:184px;border-radius:50%;margin:0 auto;display:flex;align-items:center;justify-content:center;border:8px solid rgba(255,255,255,.6);box-shadow:0 0 0 4px currentColor}
.step-ribbon{margin:26px auto 0;width:200px;height:42px;background:var(--c);color:var(--white);font-weight:600;font-size:22px;display:flex;align-items:center;justify-content:center;gap:12px;clip-path:polygon(0 0,88% 0,100% 50%,88% 100%,0 100%,8% 50%)}

/* contact */
.contact{position:absolute;left:0;top:2192px;width:590px;height:670px;background:var(--purple)}
.contact h2{position:absolute;left:0;width:590px;top:38px;text-align:center;color:var(--white);font-size:36px;font-weight:700}
.field{position:absolute;left:90px;width:455px;height:58px;border:2px solid var(--white);color:var(--white);font-weight:600;font-size:17px;padding:14px 18px}
.btn-submit{position:absolute;left:90px;top:580px;width:455px;height:58px;background:var(--white);color:var(--ink);font-weight:600;font-size:17px;display:flex;align-items:center;justify-content:center}
.map{position:absolute;left:590px;top:2192px;width:610px;height:670px;background:radial-gradient(ellipse at 55% 45%,#2d6fc4 0%,#123a82 45%,#061538 100%)}
.map-tag{position:absolute;left:140px;top:300px;width:265px;height:58px;background:var(--white);display:flex;align-items:center;gap:12px;padding-left:18px;font-weight:600;font-size:16px;color:var(--ink)}

/* newsletter + footer */
.footer{position:absolute;left:0;top:3010px;width:1200px;height:550px;background:var(--black)}
.newsletter{position:absolute;left:100px;top:2910px;width:1000px;height:220px;background:var(--white);border-radius:70px;box-shadow:0 4px 12px rgba(0,0,0,.25)}
.newsletter h2{position:absolute;left:0;width:1000px;top:24px;text-align:center;font-size:34px;font-weight:700}
.news-input{position:absolute;left:50px;top:96px;width:740px;height:82px;background:var(--purple);color:var(--white);font-size:16px;font-weight:500;display:flex;align-items:center;padding-left:40px}
.news-btn{position:absolute;left:790px;top:96px;width:160px;height:82px;background:var(--green);color:var(--white);font-weight:600;font-size:17px;display:flex;align-items:center;justify-content:center}
.foot-brand{position:absolute;left:70px;top:3200px;width:260px;display:flex;flex-direction:column;align-items:center;gap:12px}
.foot-brand .brand-name{color:var(--white);font-size:28px}
.social{position:absolute;left:130px;top:3340px;display:flex;gap:12px}
.social span{width:30px;height:30px;background:var(--white);border-radius:4px}
.foot-col{position:absolute;top:3220px;color:var(--white);font-size:15px}
.foot-col h3{font-size:16px;font-weight:600;margin-bottom:22px}
.foot-col li{list-style:none;margin-bottom:18px}
.contact-row{display:flex;align-items:center;gap:16px;margin-bottom:20px;line-height:1.3}
.contact-row .sq{width:30px;height:30px;border-radius:6px;background:var(--white);flex:none;display:flex;align-items:center;justify-content:center}
.foot-rule{position:absolute;left:0;top:3480px;width:1200px;height:1px;background:#333}
.copyright{position:absolute;left:0;width:1200px;top:3508px;text-align:center;color:var(--white);font-size:14px}
</style>
</head>
<body>

<header class="topbar">
  <div class="brand">
    <div class="brand-dot"></div>
    <div>
      <div class="brand-name">BRV MENTORING</div>
      <div class="brand-sub">Vendrixo</div>
    </div>
  </div>
  <nav class="nav"><span>Home</span><span>About Us</span><span>Services</span><span>Contact Us</span></nav>
  <div class="btn-download">DOWNLOAD</div>
  <div class="infobar">
    <div class="info-item"><span class="info-icon"><svg width="16" height="16" viewBox="0 0 24 24"><path fill="#5b2d8e" d="M6.6 10.8a15 15 0 0 0 6.6 6.6l2.2-2.2c.3-.3.7-.4 1-.2 1.1.4 2.3.6 3.6.6.6 0 1 .4 1 1V20c0 .6-.4 1-1 1C10.6 21 3 13.4 3 4c0-.6.4-1 1-1h3.5c.6 0 1 .4 1 1 0 1.3.2 2.5.6 3.6.1.3 0 .7-.2 1z"/></svg></span>+1 555 014 2290</div>
    <div class="info-item"><span class="info-icon"><svg width="16" height="16" viewBox="0 0 24 24"><path fill="#5b2d8e" d="M2 5h20v14H2zm2 2v.5l8 5 8-5V7l-8 5z"/></svg></span>info@brvmentoring.com</div>
    <div class="info-item"><span class="info-icon"><svg width="16" height="16" viewBox="0 0 24 24"><path fill="#5b2d8e" d="M12 2a7 7 0 0 0-7 7c0 5 7 13 7 13s7-8 7-13a7 7 0 0 0-7-7zm0 9.5A2.5 2.5 0 1 1 12 6.5a2.5 2.5 0 0 1 0 5z"/></svg></span>BRV Mentoring, Suite 118</div>
  </div>
</header>

<section class="hero" role="img" aria-label="Photo of a coach presenting at a whiteboard to a group in a bright office">
  <div class="hero-shade"></div>
  <h1 class="hero-text">WELCOME TO<br>BRV MENTORING</h1>
  <div class="btn-start">GET STARTED</div>
</section>

<h2 class="section-title" style="top:880px">OUR SERVICES</h2>

<div class="service" style="left:120px">
  <div class="service-top" style="background:var(--purple)"></div>
  <div class="service-icon"><svg width="90" height="80" viewBox="0 0 90 80" fill="none" stroke="#222" stroke-width="3"><rect x="30" y="6" width="54" height="36"/><circle cx="16" cy="22" r="8"/><path d="M4 70V44q0-8 12-8h22M16 36v34M38 36l8-6"/></svg></div>
  <div class="service-label" style="background:var(--purple)">COACHING <svg width="30" height="14" viewBox="0 0 30 14"><path d="M0 7h26M20 1l7 6-7 6" stroke="#fff" stroke-width="2.5" fill="none"/></svg></div>
</div>
<div class="service" style="left:460px">
  <div class="service-top" style="background:var(--green)"></div>
  <div class="service-icon"><svg width="90" height="80" viewBox="0 0 90 80" fill="none" stroke="#222" stroke-width="3"><rect x="14" y="6" width="62" height="40"/><path d="M45 46v10M30 74l15-18 15 18"/><circle cx="45" cy="24" r="7"/></svg></div>
  <div class="service-label" style="background:var(--green)">LEARNING <svg width="30" height="14" viewBox="0 0 30 14"><path d="M0 7h26M20 1l7 6-7 6" stroke="#fff" stroke-width="2.5" fill="none"/></svg></div>
</div>
<div class="service" style="left:800px">
  <div class="service-top" style="background:var(--blue)"></div>
  <div class="service-icon"><svg width="90" height="80" viewBox="0 0 90 80"><rect x="10" y="30" width="70" height="44" fill="#222"/><circle cx="45" cy="26" r="18" fill="none" stroke="#222" stroke-width="8" stroke-dasharray="7 5"/><circle cx="45" cy="26" r="7" fill="#222"/></svg></div>
  <div class="service-label" style="background:var(--blue)">SOFTWARE <svg width="30" height="14" viewBox="0 0 30 14"><path d="M0 7h26M20 1l7 6-7 6" stroke="#fff" stroke-width="2.5" fill="none"/></svg></div>
</div>

<section class="about">
  <h2>ABOUT US</h2>
  <p>Lorem ipsum dolor sit amet, consectetur adipiscing elit, sed do eiusmod tempor incididunt ut labore et dolore magna aliqua. Ut enim ad minim veniam, quis nostrud exercitation ullamco laboris nisi ut aliquip ex ea commodo consequat. Duis aute irure dolor in reprehenderit in voluptate velit esse cillum dolore eu fugiat nulla pariatur.</p>
  <div class="btn-read">READ MORE</div>
  <div class="about-photo" role="img" aria-label="Photo of a speaker presenting to a seated audience"></div>
</section>

<h2 class="section-title" style="top:1760px">HOW IT WORKS</h2>

<div class="step" style="left:60px;--c:var(--orange);color:var(--orange)">
  <div class="step-circle" style="background:var(--orange)"><svg width="80" height="60" viewBox="0 0 80 60" fill="#fff"><circle cx="40" cy="16" r="11"/><circle cx="16" cy="22" r="8"/><circle cx="64" cy="22" r="8"/><path d="M22 58q0-26 18-26t18 26zM2 56q0-20 14-20 6 0 9 3-6 7-6 17zM78 56q0-20-14-20-6 0-9 3 6 7 6 17z"/></svg></div>
  <div class="step-ribbon">1 <span>PEOPLE</span></div>
</div>
<div class="step" style="left:340px;--c:var(--brown);color:var(--brown)">
  <div class="step-circle" style="background:var(--brown)"><svg width="70" height="70" viewBox="0 0 70 70" fill="none" stroke="#fff" stroke-width="5"><circle cx="35" cy="35" r="16" stroke-dasharray="8 5" stroke-width="10"/><circle cx="35" cy="35" r="6" fill="#fff"/></svg></div>
  <div class="step-ribbon">2 <span>STRATEGY</span></div>
</div>
<div class="step" style="left:620px;--c:var(--blue);color:var(--blue)">
  <div class="step-circle" style="background:var(--blue)"><svg width="76" height="70" viewBox="0 0 76 70" fill="none" stroke="#fff" stroke-width="4"><rect x="6" y="10" width="42" height="30" rx="4"/><rect x="28" y="30" width="42" height="30" rx="4"/><path d="M36 45l6 6 12-12"/></svg></div>
  <div class="step-ribbon">3 <span>EXECUTION</span></div>
</div>
<div class="step" style="left:900px;--c:var(--green);color:var(--green)">
  <div class="step-circle" style="background:var(--green)"><svg width="80" height="70" viewBox="0 0 80 70" fill="none" stroke="#fff" stroke-width="4"><rect x="30" y="8" width="40" height="24" rx="3"/><circle cx="50" cy="20" r="5"/><path d="M4 56l14-14h14l10 6h14M4 66h40l26-14"/></svg></div>
  <div class="step-ribbon">4 <span>CASH</span></div>
</div>

<section class="contact">
  <h2>CONTACT ME</h2>
  <div class="field" style="top:112px">Name</div>
  <div class="field" style="top:188px">Email</div>
  <div class="field" style="top:264px">Phone Number</div>
  <div class="field" style="top:340px;height:210px">Message</div>
  <div class="btn-submit">SUBMIT</div>
</section>
<div class="map" role="img" aria-label="Glowing world map background showing the office location">
  <div class="map-tag"><svg width="22" height="28" viewBox="0 0 24 30"><path fill="#e0302a" d="M12 0A11 11 0 0 0 1 11c0 8 11 19 11 19s11-11 11-19A11 11 0 0 0 12 0zm0 15a4 4 0 1 1 0-8 4 4 0 0 1 0 8z"/></svg>BRV MENTORING</div>
</div>

<footer class="footer"></footer>
<section class="newsletter">
  <h2>NEWSLETTER</h2>
  <div class="news-input">Enter Email Address</div>
  <div class="news-btn">SUBSCRIBE</div>
</section>

<div class="foot-brand">
  <div class="brand-dot"></div>
  <div class="brand-name">BRV MENTORING</div>
</div>
<div class="social"><span></span><span></span><span></span><span></span></div>

<div class="foot-col" style="left:420px">
  <h3>QUICK LINKS</h3>
  <ul><li>Home</li><li>About Us</li><li>Services</li><li>Contact Me</li></ul>
</div>
<div class="foot-col" style="left:636px">
  <h3>HELP LINKS</h3>
  <ul><li>Privacy Policy</li><li>Terms &amp; Conditions</li></ul>
</div>
<div class="foot-col" style="left:862px">
  <h3>CONTACT DETAILS</h3>
  <div class="contact-row"><span class="sq"><svg width="14" height="18" viewBox="0 0 24 30"><path fill="#000" d="M12 0A11 11 0 0 0 1 11c0 8 11 19 11 19s11-11 11-19A11 11 0 0 0 12 0zm0 15a4 4 0 1 1 0-8 4 4 0 0 1 0 8z"/></svg></span><span>brv mentoring, 52 Elm Row<br>us - 310562</span></div>
  <div class="contact-row"><span class="sq"><svg width="16" height="16" viewBox="0 0 24 24"><path fill="#000" d="M6.6 10.8a15 15 0 0 0 6.6 6.6l2.2-2.2c.3-.3.7-.4 1-.2 1.1.4 2.3.6 3.6.6.6 0 1 .4 1 1V20c0 .6-.4 1-1 1C10.6 21 3 13.4 3 4c0-.6.4-1 1-1h3.5c.6 0 1 .4 1 1 0 1.3.2 2.5.6 3.6.1.3 0 .7-.2 1z"/></svg></span><span>+1 555 014 2290</span></div>
  <div class="contact-row"><span class="sq"><svg width="16" height="16" viewBox="0 0 24 24"><path fill="#000" d="M2 5h20v14H2zm2 2v.5l8 5 8-5V7l-8 5z"/></svg></span><span>info@brvmentoring.com</span></div>
</div>

<div class="foot-rule"></div>
<div class="copyright">© 2021 copyright BRV MENTORING All Rights Reserved</div>

</body>
</html>
```